Marrowgate Auctions Business Cards Design Needed

I need a business card design that is modern looking - double sided (maybe just my logo on the back, but open to suggestions) - the overall design is up to you. I want it to be easy to read - not over the top flashy. I already have a company logo which I uploaded so that needs to be used. The colors of my logo are the colors I want on the card... so blue and gray (do need to match the logo colors).

Requirements
Must have
• Would like the card to be sleek, modern and easy to ready

```html
<!DOCTYPE html>
<html lang="en">
<head>
<meta charset="utf-8">
<title>Marrowgate Auctions – Business Cards</title>
<link rel="stylesheet" href="https://fonts.googleapis.com/css2?family=Source+Sans+3:ital,wght@0,400;0,600;1,400;1,700&display=swap">
<style>
  :root {
    --page: #ffffff;
    --card-front: #060606;
    --card-back: #0a0b0d;
    --brand-blue: #2a74b8;
    --brand-gray: #5a5b5d;
    --text-light: #eeeeee;
  }
  html, body {
    margin: 0;
    padding: 0;
    width: 1200px;
    height: 1200px;
    overflow: hidden;
    background: var(--page);
    font-family: "Source Sans 3", "Myriad Pro", sans-serif;
  }
  .canvas {
    position: relative;
    width: 1200px;
    height: 1200px;
  }
  .card {
    position: absolute;
    left: 180px;
    width: 840px;
    height: 480px;
    box-sizing: border-box;
    border-bottom: 4px solid var(--brand-blue);
  }
  .card--front { top: 42px; background: var(--card-front); }
  .card--back  { top: 622px; background: var(--card-back); }

  .brand-lockup {
    position: absolute;
    left: 0;
    right: 0;
    top: 150px;
    display: flex;
    flex-direction: column;
    align-items: center;
    gap: 18px;
  }
  .brand-lockup__square {
    width: 62px;
    height: 62px;
    background: var(--brand-blue);
  }
  .brand-lockup__name {
    color: var(--brand-blue);
    font-weight: 600;
    font-size: 44px;
    letter-spacing: 1px;
    text-transform: uppercase;
    line-height: 1;
  }

  .company-name {
    position: absolute;
    left: 0; right: 0;
    top: 60px;
    margin: 0;
    text-align: center;
    color: var(--brand-blue);
    font-style: italic;
    font-weight: 700;
    font-size: 70px;
    line-height: 1;
  }
  .tagline {
    position: absolute;
    left: 0; right: 0;
    top: 152px;
    margin: 0;
    text-align: center;
    color: var(--text-light);
    font-style: italic;
    font-size: 17px;
    letter-spacing: 6.2px;
    text-transform: uppercase;
  }
  .person-name {
    position: absolute;
    left: 0; right: 0;
    top: 212px;
    margin: 0;
    text-align: center;
    color: var(--text-light);
    font-weight: 600;
    font-size: 52px;
    line-height: 1;
  }
  .person-title {
    position: absolute;
    left: 0; right: 0;
    top: 283px;
    margin: 0;
    text-align: center;
    color: var(--brand-blue);
    font-size: 22px;
  }
  .contact {
    position: absolute;
    left: 250px;
    top: 326px;
    margin: 0;
    padding: 0;
    list-style: none;
  }
  .contact__item {
    display: flex;
    align-items: center;
    gap: 16px;
    height: 44px;
    color: var(--brand-blue);
    font-size: 22px;
  }
  .contact__item--phone { padding-left: 62px; }
  .contact__icon { width: 32px; height: 32px; flex: none; }
  .contact__item--phone .contact__icon { width: 24px; }
</style>
</head>
<body>
<div class="canvas">

  <section class="card card--front" aria-label="Card front">
    <div class="brand-lockup">
      <div class="brand-lockup__square"></div>
      <div class="brand-lockup__name">Marrowgate Auctions</div>
    </div>
  </section>

  <section class="card card--back" aria-label="Card back">
    <h1 class="company-name">Marrowgate Auctions, Inc.</h1>
    <p class="tagline">Improving charity auctions nationwide</p>
    <h2 class="person-name">Owen Hartley</h2>
    <p class="person-title">Owner/President - Auctioneer</p>
    <ul class="contact">
      <li class="contact__item contact__item--phone">
        <svg class="contact__icon" viewBox="0 0 24 32" aria-hidden="true">
          <path d="M6 2 L10 2 L11 9 L8 11 C9 16 11 21 14 24 L17 22 L22 27 L19 30 C10 30 3 18 3 8 Z" fill="none" stroke="#eeeeee" stroke-width="2" stroke-linejoin="round"/>
        </svg>
        <span>702-555-0148</span>
      </li>
      <li class="contact__item">
        <svg class="contact__icon" viewBox="0 0 32 32" aria-hidden="true">
          <rect x="1" y="6" width="30" height="21" fill="none" stroke="#eeeeee" stroke-width="2"/>
          <path d="M1 6 L16 18 L31 6 M1 27 L12 15 M31 27 L20 15" fill="none" stroke="#eeeeee" stroke-width="2"/>
        </svg>
        <span>marrowgateauctions@mail.com</span>
      </li>
      <li class="contact__item">
        <svg class="contact__icon" viewBox="0 0 32 32" aria-hidden="true">
          <g fill="none" stroke="#eeeeee" stroke-width="1.8">
            <circle cx="16" cy="16" r="14"/>
            <ellipse cx="16" cy="16" rx="6" ry="14"/>
            <line x1="16" y1="2" x2="16" y2="30"/>
            <line x1="2" y1="16" x2="30" y2="16"/>
            <path d="M5 9 H27 M5 23 H27"/>
          </g>
        </svg>
        <span>http://bidlanternhelp.com/</span>
      </li>
    </ul>
  </section>

</div>
</body>
</html>
```